ROLL-ON-VERANDA Business Card Design

Please do not submit more than one design per designer. Both the front and the back must be submitted as a single design. Please use all of the attached files to design a two-sided business card. Do not use tiny text that is hard to read. Do not put text or images too close to the edges where it might get cut off during printing. The card should be horizontal. Please do not send me the same design that I attached showing the business information. Be creative.

One file is marked as the primary logo for company. Other files are marked as secondary. All logos should be incorporated into the design with a focus on the primary one being bigger.

```html
<!DOCTYPE html>
<html lang="en">
<head>
<meta charset="utf-8">
<title>ROLL-ON-VERANDA Business Card</title>
<link href="https://fonts.googleapis.com/css2?family=Jost:wght@400;500;800&display=swap" rel="stylesheet">
<style>
  :root {
    --page-bg: #eeeeee;
    --card-white: #ffffff;
    --card-foot: #c9c9c9;
    --ink: #111111;
    --ink-soft: #6b6b6b;
    --rule: #777777;
    --dark-1: #161616;
    --dark-2: #3a3a3a;
    --badge-red: #c8232c;
    --badge-blue: #1f3a7a;
    --badge-gold: #b8962e;
    --badge-navy: #16244f;
  }
  * { margin: 0; padding: 0; box-sizing: border-box; }
  html, body { width: 1200px; height: 619px; overflow: hidden; }
  body {
    background: var(--page-bg);
    font-family: "Jost", "Futura", sans-serif;
    position: relative;
  }
  .card {
    position: absolute;
    top: 154px;
    width: 540px;
    height: 310px;
    border-radius: 14px;
    overflow: hidden;
    box-shadow: 0 6px 18px rgba(0,0,0,0.18);
  }
  .card-front { left: 40px; background: var(--card-white); border-bottom: 16px solid var(--card-foot); }
  .card-back { left: 620px; background: linear-gradient(160deg, var(--dark-1) 0%, var(--dark-2) 100%); }

  .boat-art {
    position: absolute;
    border-radius: 40% 60% 30% 50%;
  }
  .card-front .boat-art {
    left: 166px; top: 34px; width: 196px; height: 70px;
    background: radial-gradient(ellipse at 55% 55%, #1a1a1a 0%, #6a6a6a 55%, rgba(255,255,255,0) 75%);
  }
  .card-back .boat-art {
    left: 160px; top: 72px; width: 210px; height: 72px;
    background: radial-gradient(ellipse at 55% 55%, #f2f2f2 0%, #9a9a9a 50%, rgba(60,60,60,0) 75%);
  }
  .wave-decor {
    position: absolute; left: 0; top: 0; width: 540px; height: 200px;
    background: linear-gradient(175deg, rgba(255,255,255,0.06) 0%, rgba(255,255,255,0.02) 50%, rgba(0,0,0,0) 100%);
  }
  .brand-name {
    position: absolute;
    text-align: center;
    font-weight: 800;
    white-space: nowrap;
  }
  .card-front .brand-name {
    left: 140px; top: 108px; width: 260px;
    font-size: 22px; color: var(--ink);
  }
  .card-back .brand-name {
    left: 0; top: 152px; width: 540px;
    font-size: 25px; color: #ffffff;
  }

  .badges { position: absolute; left: 426px; top: 30px; }
  .badges svg { display: block; }

  .name-row {
    position: absolute; left: 0; top: 184px; width: 540px; height: 30px;
  }
  .name-row .rule { position: absolute; top: 15px; height: 3px; background: var(--rule); }
  .rule-left { left: 0; width: 24px; }
  .rule-right { left: 314px; right: 0; }
  .holder-name {
    position: absolute; left: 34px; top: 0;
    font-size: 21px; font-weight: 500; color: var(--ink); white-space: nowrap;
  }
  .credentials, .services {
    position: absolute; top: 220px;
    font-size: 14.5px; line-height: 18px; color: var(--ink-soft);
  }
  .credentials { left: 34px; }
  .services { right: 24px; text-align: right; }

  .contact-line {
    position: absolute; left: 0; bottom: 34px; width: 100%;
    text-align: center; color: #ffffff; font-size: 13.5px; letter-spacing: 0.2px; white-space: nowrap;
  }
</style>
</head>
<body>
  <section class="card card-front">
    <div class="boat-art" role="img" aria-label="Illustration of a cabin boat cruising"></div>
    <div class="brand-name">ROLL-ON-VERANDA</div>
    <div class="badges">
      <svg width="92" height="90" viewBox="0 0 92 90" aria-hidden="true">
        <circle cx="22" cy="20" r="18" fill="var(--badge-red)"/>
        <circle cx="68" cy="20" r="16" fill="var(--badge-blue)"/>
        <circle cx="24" cy="68" r="17" fill="var(--badge-gold)"/>
        <circle cx="68" cy="68" r="17" fill="var(--badge-navy)"/>
      </svg>
    </div>
    <div class="name-row">
      <span class="rule rule-left"></span>
      <span class="holder-name">Captain Dana R. Holloway</span>
      <span class="rule rule-right"></span>
    </div>
    <div class="credentials">
      NMCB Licensed Master Captain<br>
      CBTA Certified Instructor<br>
      Graduate Degree<br>
      Veteran
    </div>
    <div class="services">
      Providing Hands on Boat<br>
      training Captaining Services<br>
      and Deliveries In the<br>
      Harbor Bay Area.
    </div>
  </section>

  <section class="card card-back">
    <div class="wave-decor" role="img" aria-label="Soft wave pattern in dark grey tones"></div>
    <div class="boat-art" role="img" aria-label="Illustration of a cabin boat cruising in white"></div>
    <div class="brand-name">ROLL-ON-VERANDA</div>
    <div class="contact-line">www.roll-on-veranda.com &nbsp;|&nbsp; service@rollonveranda.com &nbsp;|&nbsp; Text: 555 014 2288</div>
  </section>
</body>
</html>
```